indépendant en tant que Massothérapeute et Préparateur Mental, j'ai besoin de ...

Massothérapeute et préparateur mental indépendant, je recherche une carte de visite sobre et dynamique, sans images liées au massage ou à la préparation mentale mais intégrant mon logo. Les couleurs que j'aime bien sont : Blanc, gris, anthracite, noir et jaune

carte de préférence Horizontale
neutre qui puisse toucher le deux domaines Massothérapie et préparation mentale

Requirements
Must have
• mon projet doit intégrer au recto:
LOGO
Loïc Bardemaz
078 315 26 48
info@loicbardemaz-exemple.ch
et éventuellement www.loicbardemaz-exemple.ch

et au verso les deux adresses:

Chemin des Grèvelins 7B
1400 Yverdon-les-Bains

Avenue des Mélèzes 9
1700 Fribourg

Should not have
• mon projet ne doit pas contenir d'image en liens avec le massage ni la préparation mentale.

```html
<!DOCTYPE html>
<html lang="fr">
<head>
<meta charset="utf-8">
<title>Loïc Bardemaz – Carte de visite</title>
<link rel="stylesheet" href="https://fonts.googleapis.com/css2?family=Questrial&display=swap">
<style>
  :root {
    --page: #fefefe;
    --card: #231f20;
    --card-edge: #6d6d6d;
    --ink-light: #ffffff;
    --accent: #f5a623;
    --ghost: #373435;
  }
  * { margin: 0; padding: 0; box-sizing: border-box; }
  html, body {
    width: 1200px; height: 1200px; overflow: hidden;
    background: var(--page);
    font-family: "Questrial", "Century Gothic", sans-serif;
  }
  .sheet { position: relative; width: 1200px; height: 1200px; }
  .card {
    position: absolute; top: 454px;
    width: 496px; height: 282px;
    background: var(--card);
    border: 2px solid var(--card-edge);
    overflow: hidden;
  }
  .card--front { left: 75px; }
  .card--back { left: 617px; }

  .brand { position: absolute; left: 45px; top: 48px; display: flex; align-items: center; gap: 12px; }
  .brand__mark { width: 34px; height: 34px; background: var(--ink-light); }
  .brand__name { color: var(--ink-light); font-size: 25px; line-height: 1; letter-spacing: 0.5px; }
  .brand__role {
    color: var(--ink-light); font-size: 9.5px; letter-spacing: 0.8px;
    text-transform: uppercase; margin-top: 5px;
  }

  .contact { position: absolute; left: 0; right: 0; top: 138px; text-align: center; }
  .contact__name { color: var(--ink-light); font-size: 19px; line-height: 1.1; }
  .contact__phone { color: var(--accent); font-size: 15px; margin-top: 2px; }

  .links {
    position: absolute; left: 0; right: 0; top: 245px;
    text-align: center; color: var(--ink-light); font-size: 14px;
  }
  .links__divider { color: var(--accent); margin: 0 8px; }

  .addresses { position: absolute; left: 47px; top: 56px; color: var(--accent); font-size: 15.5px; line-height: 19px; }
  .address + .address { margin-top: 18px; }

  .ghost-name {
    position: absolute; left: -6px; bottom: -22px;
    color: var(--ghost); font-size: 92px; line-height: 1; white-space: nowrap;
  }
</style>
</head>
<body>
<main class="sheet">
  <section class="card card--front" aria-label="Recto">
    <div class="brand">
      <span class="brand__mark"></span>
      <div>
        <div class="brand__name">Loïc Bardemaz</div>
        <div class="brand__role">Massothérapeute / Préparateur Mental</div>
      </div>
    </div>
    <div class="contact">
      <p class="contact__name">Loïc Bardemaz</p>
      <p class="contact__phone">078 315 26 48</p>
    </div>
    <p class="links">info@loicbardemaz-exemple.ch<span class="links__divider">|</span>www.loicbardemaz-exemple.ch</p>
  </section>

  <section class="card card--back" aria-label="Verso">
    <div class="ghost-name" aria-hidden="true">Loïc Bardemaz</div>
    <div class="addresses">
      <p class="address">Chemin des Grèvelins 7B<br>1400 Yverdon-les-Bains</p>
      <p class="address">Avenue des Mélèzes 9<br>1700 Freiburg</p>
    </div>
  </section>
</main>
</body>
</html>
```